Kindro - Bringing Warmth and Quality to Senior Living

We are a new company based in Sydney, Australia. We have developed a state-of-the-art app for communication between aged care facilities and families.

Kindro has been developed for facilities to augment the best possible care by providing easy, safe and secure communication for families to stay in touch with their loved ones.
Updates

the website needs to be designed so we can add functionality including multilingual support. display in different languages.we also require enquiry and email/data base function. we want it simple and clean so its responsive. the target audience will be 40+ in age. there will be a video on home page. would like to start with 6 pages/ subjects -homepage -about us -our solution -demonstration page, this will be a page that contains videos of people using our product -customer testimonials -contact us

Target Market(s)

Aged care facilities.
Families (over 40’s age group) who are looking for a facility for their loved ones.

Number of Pages Required

5+ page

Font styles to use
Sans Serif

Colors
faa54b
ffffff
0255a3

Requirements
Must have
• - Our corporate colour is #EE8811.
• - If you're using stock photography, please use brimlo prints photos as we have a license for their photos.
• - The design needs to be responsive (mobile and desktop)
• -White space on each page
Nice to have
• -need to leave a place for a future animation video to be added in on the home tab
Should not have
• we don't want flash technology

```html
<!DOCTYPE html>
<html lang="en">
<head>
<meta charset="utf-8">
<title>Kindro - Bringing Warmth and Quality to Senior Living</title>
<link rel="stylesheet" href="https://fonts.googleapis.com/css2?family=Poppins:wght@300;400;500;600;700;800&display=swap">
<style>
:root{
  --blue:#0d55a3;
  --navy:#0c3f74;
  --orange:#ee8811;
  --orange-soft:#faa54b;
  --white:#ffffff;
  --ink:#333a44;
  --muted:#6a6f78;
  --ghost:#e9edf3;
}
*{box-sizing:border-box;margin:0;padding:0}
html,body{width:1200px;height:3881px;overflow:hidden}
body{font-family:'Poppins',sans-serif;color:var(--ink);background:var(--white);position:relative}
.abs{position:absolute}
.btn{position:absolute;display:flex;align-items:center;justify-content:center;height:32px;border-radius:16px;font-size:12px;color:var(--white);background:var(--blue);border-left:3px solid var(--orange)}
.btn.orange{background:var(--orange);border-left:none}
.btn.outline{background:var(--blue);border-left:3px solid var(--white)}
.ghost{position:absolute;left:0;width:1200px;text-align:center;font-weight:800;letter-spacing:14px;color:var(--ghost);font-size:70px;line-height:1}
.title{position:absolute;left:0;width:1200px;text-align:center;font-weight:600;font-size:32px;color:var(--blue);line-height:1}
.title span{color:var(--orange)}
.title.light{color:var(--white)}
.divider{position:absolute;height:12px;display:flex;align-items:center;gap:12px}
.divider i{flex:1;height:1px;background:var(--orange)}
.divider b{width:10px;height:10px;border:1.5px solid var(--orange);border-radius:50%}
.divider.light i{background:rgba(255,255,255,.6)}
.divider.light b{border-color:var(--white)}

.nav{position:absolute;top:0;left:0;width:1200px;height:56px;background:var(--white);box-shadow:0 2px 6px rgba(0,0,0,.08);z-index:5}
.brand{position:absolute;left:233px;top:12px;display:flex;align-items:center;gap:8px;font-size:26px;font-weight:600;color:var(--orange)}
.brand i{width:26px;height:26px;border-radius:50%;background:var(--orange)}
.menu{position:absolute;left:458px;top:20px;display:flex;gap:26px;font-size:12px;color:var(--ink)}
.menu .on{color:var(--orange);border-bottom:1px solid var(--orange);padding-bottom:6px}

.hero{position:absolute;top:56px;left:0;width:1200px;height:530px;background:linear-gradient(100deg,#f3e6d8 0%,#e8d2b9 40%,#b48a6a 70%,#7d6a5e 100%)}
.hero-title{position:absolute;left:233px;top:190px;font-size:37px;font-weight:600;color:var(--blue);line-height:52px}

.about-frame-l{position:absolute;left:238px;top:736px;width:48px;height:335px;border:5px solid var(--blue);border-right:none}
.about-frame-r{position:absolute;left:910px;top:760px;width:48px;height:288px;border:5px solid var(--orange);border-left:none}
.about-photo{position:absolute;left:252px;top:752px;width:362px;height:302px;background:var(--white);box-shadow:0 2px 10px rgba(0,0,0,.15);padding:12px}
.about-photo div{width:100%;height:100%;background:linear-gradient(135deg,#3d3a36,#8c7a62 55%,#d9c8ad)}
.about-card{position:absolute;left:580px;top:772px;width:364px;height:262px;background:var(--white);box-shadow:0 2px 12px rgba(0,0,0,.15);padding:18px 20px}
.about-card h3{font-size:15px;font-weight:500;color:var(--orange)}
.about-card h3 span{color:var(--blue)}
.about-card .dot{width:10px;height:10px;border:1.5px solid var(--orange);border-radius:50%;margin:10px 0 10px}
.about-card p{font-size:11px;line-height:18.7px;color:var(--muted)}

.band{position:absolute;top:1182px;left:0;width:1200px;height:225px;background:linear-gradient(135deg,#2c67a5,var(--navy) 60%,#0a3563)}
.band h2{position:absolute;top:38px;width:1200px;text-align:center;font-size:28px;font-weight:500;color:var(--white)}
.band h2 span{color:var(--orange)}
.band p{position:absolute;top:108px;width:1200px;text-align:center;font-size:14px;color:var(--white);letter-spacing:.3px}

.sol-text{position:absolute;left:233px;top:1585px;width:330px}
.sol-text h3{font-size:16px;font-weight:600;color:var(--blue)}
.sol-text h3 span{color:var(--orange)}
.sol-rule{display:flex;align-items:center;gap:8px;margin:14px 0 18px}
.sol-rule b{width:10px;height:10px;border:1.5px solid var(--orange);border-radius:50%}
.sol-rule i{width:190px;height:1px;background:var(--orange)}
.sol-text p{font-size:11px;line-height:18.7px;color:var(--muted)}

.facilities{position:absolute;top:1917px;left:0;width:1200px;height:444px;background:linear-gradient(180deg,#4b4944,#34352f 50%,#2c3326)}
.fac-card{position:absolute;width:221px;height:78px;background:rgba(255,255,255,.2);padding:20px 10px 0 43px;font-size:12px;line-height:17px;color:var(--white)}
.fac-ico{position:absolute;width:44px;height:44px;border-radius:50%;background:var(--orange);border:3px solid rgba(255,255,255,.85)}

.member{position:absolute;top:2529px;width:231px;height:268px}
.member .ph{position:absolute;inset:0;background:linear-gradient(180deg,#cfd3d8,#8a96a6)}
.member .cl{position:absolute;left:0;top:0;width:22px;height:22px;border-left:4px solid var(--orange);border-top:4px solid var(--orange)}
.member .cr{position:absolute;right:0;bottom:0;width:22px;height:22px;border-right:4px solid var(--orange);border-bottom:4px solid var(--orange)}
.member .tag{position:absolute;left:0;padding:3px 12px;font-size:11px;color:var(--white)}
.member .name{top:196px;background:var(--orange)}
.member .role{top:229px;background:var(--blue)}
.member.hover .ph{background:#3f4247}
.member.hover .tri-a{position:absolute;left:0;top:0;width:0;height:0;border-top:58px solid var(--orange);border-right:58px solid transparent}
.member.hover .tri-b{position:absolute;right:0;bottom:0;width:0;height:0;border-bottom:58px solid var(--orange);border-left:58px solid transparent}
.member.hover .info{position:absolute;left:0;top:52px;width:231px;text-align:center;color:var(--white);font-size:12px;line-height:17px}
.member.hover .info .r{color:var(--orange);font-size:11px}
.member.hover .info hr{border:none;height:1px;background:rgba(255,255,255,.4);width:170px;margin:8px auto}
.socials{display:flex;justify-content:center;gap:14px;margin-top:4px}
.socials i{width:16px;height:16px;border-radius:50%;border:1.5px solid var(--white)}

.testi{position:absolute;top:2940px;left:0;width:1200px;height:500px;background:linear-gradient(90deg,#2b2a28,#4d4841 50%,#2c2c2e)}
.t-card{position:absolute;top:3105px;width:283px;height:214px;border:1px solid var(--orange);background:rgba(0,0,0,.25);text-align:center;padding:42px 20px 0}
.t-card h4{font-size:13px;font-weight:400;color:var(--orange);margin-bottom:10px}
.t-card p{font-size:10px;line-height:15.5px;color:var(--white)}
.t-card .by{text-align:right;color:var(--orange);font-size:10px;margin-top:6px}
.t-av{position:absolute;top:-32px;left:109px;width:64px;height:64px;border-radius:50%;border:3px solid var(--orange);background:linear-gradient(135deg,#c9a78b,#6b5240)}
.t-arrow{position:absolute;top:3201px;width:24px;height:24px;border-radius:50%;border:1.5px solid var(--white)}

.contact{position:absolute;top:3440px;left:0;width:1200px;height:394px;background:#f4f5f7}
.col{position:absolute;top:3590px}
.col h5{font-size:15px;font-weight:500;color:var(--orange)}
.col-head{text-align:center;width:170px}
.col-head h5{margin-top:4px;padding-bottom:10px;border-bottom:1px solid var(--blue)}
.icon{display:block;margin:0 auto}
.links{list-style:none;font-size:11px;color:var(--ink);margin-top:12px}
.links li{height:31px}
.links li.on{color:var(--orange)}
.small{font-size:11px;color:var(--ink);line-height:17px}
.field{border-bottom:1px solid var(--blue);font-size:10px;color:var(--muted);padding-bottom:4px}
.footer{position:absolute;top:3834px;left:0;width:1200px;height:47px;background:var(--blue);color:var(--white);font-size:10px;text-align:center;line-height:47px}
</style>
</head>
<body>

<header class="nav">
  <div class="brand"><i></i>Kindro</div>
  <nav class="menu">
    <span class="on">Home</span><span>About Us</span><span>Our Solution</span><span>Demonstration</span><span>Testimonials</span><span>Contact Us</span>
  </nav>
</header>

<section class="hero" role="img" aria-label="Smiling senior couple on a sofa looking at a tablet together"></section>
<h1 class="hero-title">We Offers Families<br>Proof Of Excellent Care..</h1>
<div class="btn" style="left:233px;top:327px;width:119px">Contact Us</div>
<svg class="abs" style="left:0;top:470px" width="1200" height="130" viewBox="0 0 1200 130" aria-hidden="true">
  <path d="M0 90 C250 20 450 20 700 80 C900 125 1080 100 1200 20 L1200 130 L0 130Z" fill="#fff"/>
  <path d="M0 90 C250 20 450 20 700 80 C900 125 1080 100 1200 20" fill="none" stroke="#ee8811" stroke-width="6"/>
</svg>

<div class="ghost" style="top:560px;text-align:left;left:72px;font-size:92px">ABOUT US</div>
<div class="title" style="top:648px">About <span>Us</span></div>
<div class="divider" style="top:690px;left:524px;width:152px"><i></i><b></b><i></i></div>
<div class="about-frame-l"></div>
<div class="about-frame-r"></div>
<div class="about-photo"><div role="img" aria-label="Business team meeting around a table"></div></div>
<div class="about-card">
  <h3>Few Words <span>About Us</span></h3>
  <div class="dot"></div>
  <p>We are a Sydney based, family owned business who have combined experiences from many walks of life that have led us to produce a solution for an issue that was of great concern to us. Our backgrounds encompass 40 years of software development, decades of experience in marketing, management and service delivery and over 10 years within the childcare industry. The founders were concerned by the lack of communication during their loved ones' time in residential aged care.</p>
</div>
<div class="btn" style="left:543px;top:1110px;width:107px">Read More</div>

<section class="band">
  <h2><span>100%</span> Satisfaction Guarantee!</h2>
  <div class="divider light" style="top:84px;left:426px;width:348px"><i></i><b></b><i></i></div>
  <p>Residents privacy is ensured by the use of advanced artificial intelligence processes.</p>
  <div class="btn orange" style="left:545px;top:165px;width:107px;height:28px;font-size:11px">Contact Us</div>
</section>

<div class="ghost" style="top:1428px">OUR SOLUTION</div>
<div class="title" style="top:1483px">Our <span>Solutions</span></div>
<div class="divider" style="top:1529px;left:488px;width:224px"><i></i><b></b><i></i></div>
<div class="sol-text">
  <h3>Let's See <span>Kindro Features</span></h3>
  <div class="sol-rule"><b></b><i></i></div>
  <p>Works on all phones and tablets. Simple to use. Provides frequent resident updates to families such as meal reports, activities and visitors with associated photos and videos. Residents privacy is ensured by the use of advanced artificial intelligence processes. Kindro complies with the requirements of Privacy Act 1988 (Cth). Information is protected as required by current Australian law.</p>
</div>
<div class="btn" style="left:233px;top:1838px;width:107px">Read More</div>
<div class="abs" style="left:897px;top:1561px;width:63px;height:312px;background:var(--orange-soft)"></div>
<div class="abs" style="left:586px;top:1577px;width:48px;height:286px;border:5px solid var(--blue);border-right:none"></div>
<div class="abs" role="img" aria-label="Team joining fists over a desk with laptops" style="left:602px;top:1593px;width:338px;height:250px;background:linear-gradient(135deg,#5c5a57,#a29a8f 50%,#3d3b3a)"></div>
<div class="abs" style="left:585px;top:1705px;width:34px;height:34px;border-radius:50%;background:var(--white);border:3px solid var(--orange)"></div>
<svg class="abs" style="left:595px;top:1714px" width="14" height="16" aria-hidden="true"><path d="M12 2 L3 8 L12 14Z" fill="#ee8811"/></svg>

<section class="facilities" role="img" aria-label="Group of friends smiling outdoors, darkened"></section>
<div class="title light" style="top:1957px">Our <span>Facilities</span></div>
<div class="divider light" style="top:2006px;left:540px;width:120px"><i></i><b></b><i></i></div>
<div class="fac-card" style="left:243px;top:2060px">Offers families proof of excellent care</div>
<div class="fac-card" style="left:492px;top:2060px">Competitive advantages over other facilities.</div>
<div class="fac-card" style="left:740px;top:2060px">Very little additional work for carers and management</div>
<div class="fac-card" style="left:243px;top:2172px">Allows carers to demonstrate the quality of their work.</div>
<div class="fac-card" style="left:492px;top:2172px">Frequent contact with loved ones.</div>
<div class="fac-card" style="left:740px;top:2172px">Easier communication between residents and families.</div>
<div class="fac-ico" style="left:233px;top:2050px"></div>
<div class="fac-ico" style="left:482px;top:2050px"></div>
<div class="fac-ico" style="left:731px;top:2050px"></div>
<div class="fac-ico" style="left:233px;top:2162px"></div>
<div class="fac-ico" style="left:482px;top:2162px"></div>
<div class="fac-ico" style="left:731px;top:2162px"></div>
<div class="btn outline" style="left:545px;top:2284px;width:107px;height:28px">View All</div>

<div class="ghost" style="top:2385px">OUR TEAM</div>
<div class="title" style="top:2438px">Our <span>Team</span></div>
<div class="divider" style="top:2489px;left:518px;width:164px"><i></i><b></b><i></i></div>
<div class="member" style="left:233px">
  <div class="ph" role="img" aria-label="Portrait of a senior man in glasses and blazer"></div>
  <div class="cl"></div><div class="cr"></div>
  <div class="tag name">Martin Hale</div><div class="tag role">Lead Developer</div>
</div>
<div class="member hover" style="left:482px">
  <div class="ph" role="img" aria-label="Portrait of a woman, darkened behind details"></div>
  <div class="tri-a"></div><div class="tri-b"></div>
  <div class="info">
    Nadia Brooks<br><span class="r">Advisor</span>
    <hr>
    Co-Founder &amp; MD, Larkfield<br>Advisory +<br>Bayline Systems
    <hr>
    <div class="socials"><i></i><i></i><i></i></div>
  </div>
</div>
<div class="member" style="left:731px">
  <div class="ph" role="img" aria-label="Portrait of a smiling young man in a suit"></div>
  <div class="cl" style="border-color:var(--blue)"></div><div class="cr" style="border-color:var(--blue)"></div>
  <div class="tag name">Owen Parry</div><div class="tag role">Founder</div>
</div>
<svg class="abs" style="left:928px;top:2814px" width="36" height="22" aria-hidden="true"><path d="M2 15 H34 M30 11 L34 15 M6 7 H34 M2 7 L6 3 M2 7 L6 11 M30 19 L34 15" stroke="#0d55a3" stroke-width="1.5" fill="none"/></svg>
<div class="btn" style="left:545px;top:2855px;width:107px;height:30px">View More</div>

<section class="testi" role="img" aria-label="People in a bright room, darkened"></section>
<div class="title light" style="top:2981px">Our <span>Testimonials</span></div>
<div class="divider light" style="top:3037px;left:474px;width:252px"><i></i><b></b><i></i></div>
<div class="t-card" style="left:291px">
  <div class="t-av" role="img" aria-label="Reviewer portrait"></div>
  <h4>Improve Performance</h4>
  <p>Lorem Ipsum is simply dummy text of the printing and typesetting industry. Lorem Ipsum has been the industry's standard dummy text ever since the 1500s, when an unknown printer took a galley of type and scrambled it to make a type specimen book. It has survived not only five centuries, but</p>
  <div class="by">- Helen Marsh</div>
</div>
<div class="t-card" style="left:630px">
  <div class="t-av" role="img" aria-label="Reviewer portrait"></div>
  <h4>Improve Performance</h4>
  <p>Lorem Ipsum is simply dummy text of the printing and typesetting industry. Lorem Ipsum has been the industry's standard dummy text ever since the 1500s, when an unknown printer took a galley of type and scrambled it to make a type specimen book. It has survived not only five centuries, but</p>
  <div class="by">- Carla Dunne</div>
</div>
<div class="t-arrow" style="left:218px"></div>
<svg class="abs" style="left:223px;top:3206px" width="14" height="14" aria-hidden="true"><path d="M12 7 H2 M6 3 L2 7 L6 11" stroke="#fff" stroke-width="1.5" fill="none"/></svg>
<div class="t-arrow" style="left:958px"></div>
<svg class="abs" style="left:963px;top:3206px" width="14" height="14" aria-hidden="true"><path d="M2 7 H12 M8 3 L12 7 L8 11" stroke="#fff" stroke-width="1.5" fill="none"/></svg>
<div class="btn orange" style="left:545px;top:3365px;width:107px;height:28px">Read More</div>

<section class="contact"></section>
<div class="title" style="top:3470px">Contact <span>Us</span></div>
<div class="divider" style="top:3515px;left:540px;width:120px"><i></i><b></b><i></i></div>

<div class="col" style="left:233px">
  <h5>Quick Links</h5>
  <ul class="links">
    <li class="on">› Home</li><li>› About Us</li><li>› Our Solution</li><li>› Demonstration</li><li>› Testimonials</li><li>› Contact Us</li>
  </ul>
</div>

<div class="col col-head" style="left:383px;top:3600px">
  <svg class="icon" width="36" height="32" aria-hidden="true"><rect x="10" y="4" width="22" height="15" fill="none" stroke="#ee8811" stroke-width="1.5"/><path d="M10 4 L21 12 L32 4" fill="none" stroke="#ee8811" stroke-width="1.5"/><path d="M4 14 C4 24 10 30 18 30" fill="none" stroke="#ee8811" stroke-width="1.5"/></svg>
  <h5>Contact Us</h5>
  <div class="small" style="margin-top:10px">☏ +61 2 5550 1842</div>
  <div class="small" style="margin-top:10px;font-size:10px">✉ hello@kindro-care.example</div>
  <div class="socials" style="margin-top:14px"><i style="border-color:var(--orange)"></i><i style="border-color:var(--blue)"></i><i style="border-color:var(--blue)"></i><i style="border-color:var(--blue)"></i><i style="border-color:var(--blue)"></i></div>
</div>

<div class="col col-head" style="left:586px;top:3600px">
  <svg class="icon" width="36" height="32" aria-hidden="true"><path d="M3 15 L33 3 L25 29 L17 19Z M17 19 L33 3" fill="none" stroke="#ee8811" stroke-width="1.5"/></svg>
  <h5>Newsletter</h5>
  <div class="small" style="margin-top:10px;font-size:10px;line-height:16px">Subscribe to our Newsletter and stay up to date with all event coming straight in your</div>
  <div style="margin:8px auto 0;width:154px;height:22px;border:1px solid var(--blue);border-radius:11px;font-size:9px;text-align:left;padding:4px 12px;color:var(--muted)">Email</div>
  <div style="margin:10px auto 0;width:86px;height:24px;border-radius:12px;background:var(--orange);color:#fff;font-size:11px;line-height:24px">Subscribe</div>
</div>

<div class="col col-head" style="left:793px;top:3600px;width:170px">
  <svg class="icon" width="40" height="32" aria-hidden="true"><rect x="3" y="10" width="26" height="18" fill="none" stroke="#ee8811" stroke-width="1.5"/><path d="M3 10 L16 20 L29 10" fill="none" stroke="#ee8811" stroke-width="1.5"/><circle cx="30" cy="9" r="7" fill="#fff" stroke="#ee8811" stroke-width="1.5"/></svg>
  <h5 style="border:none;padding-bottom:0">Get In Touch</h5>
  <div class="field" style="text-align:left;margin-top:20px">Name</div>
  <div class="field" style="text-align:left;margin-top:16px">Email</div>
  <div class="field" style="text-align:left;margin-top:40px">Subject</div>
  <div style="margin:12px auto 0;width:62px;height:20px;border-radius:10px;background:var(--orange);color:#fff;font-size:10px;line-height:20px">Send</div>
</div>

<footer class="footer">© Kindro 2019. All rights reserved.</footer>

</body>
</html>
```